Lydia Vandermere personal business/name cards and stationery brief

I am looking for a simple design on my personal business cards, that I may use for all my stationery. All my stationery would be cream or ivory textured card, or cream/ivory quality paper. I am director of my family company and also property developer. But am wishing to have basic business cards that I can use across both businesses. I do not wish to have a title, just my initials as a focal point.
Target Market(s)
These are my personal business cards and stationery. I am looking for an elegant, relatively understated design that exudes wealth. There is no target audience, other than clients or people I already do business with. However design must be stylish and timeless.
If I am handing out my business card to anyone I do not do business with, or they are not contracting to me or my company currently, then i would like the target audience to wish they were.
I am 54 yeas of age, and my business cards must denote respect and class.
Industry/Entity Type
Business
Contact Information for Business Card
LV
Lydia Vandermere
Justice of the Peace
Possible rear of card
Mobile number
Email
Font styles to use
Requirements
Must have
- LV to be somehow entwined as a logo on the front of the card above my name
- These cards must state that I am a Justice of the Peace
- Colours only ivory or cream card with texture, and gold elegant font.
- Must be able to be used on all my stationery products
- Must be elegant, timeless and not cluttered
- Below are just some design I like. There is something in each design I like.
Nice to have
- I would like my initials to be the centre piece of the card. Somehow entwined together elegantly in a logo of sorts that I can use across all my stationery. But if not my initials, then something that is different and stands out from the rest.
Should not have
- Not gawdy or young. No colour. Nothing outlandish.

```html
<!DOCTYPE html>
<html lang="en">
<head>
<meta charset="utf-8">
<title>Lydia Vandermere — Business Card</title>
<link rel="stylesheet" href="https://fonts.googleapis.com/css2?family=Parisienne&family=Montserrat:wght@300;400&display=swap">
<style>
  :root {
    --backdrop: #ebe6dd;
    --ivory: #f4f0e3;
    --ivory-edge: #e2dccb;
    --slate: #7b7a76;
    --gold: #b8921f;
    --gold-light: #d4b043;
    --ink: #3e3a33;
  }
  * { margin: 0; padding: 0; box-sizing: border-box; }
  html, body {
    width: 1200px;
    height: 822px;
    overflow: hidden;
    background: var(--backdrop);
  }
  .canvas {
    width: 1200px;
    height: 822px;
    display: flex;
    flex-direction: column;
    align-items: center;
    justify-content: center;
    gap: 50px;
  }
  .card {
    width: 560px;
    height: 311px;
    position: relative;
    box-shadow: 0 6px 18px rgba(60, 50, 30, 0.18);
    display: flex;
    flex-direction: column;
    align-items: center;
  }
  .card--front {
    background: var(--ivory);
    border: 1px solid var(--ivory-edge);
  }
  .card--back {
    background: var(--slate);
    justify-content: center;
  }
  .monogram {
    font-family: "Montserrat", sans-serif;
    font-weight: 300;
    font-size: 44px;
    letter-spacing: 2px;
    color: var(--gold);
    line-height: 1;
  }
  .card--front .monogram { margin-top: 62px; }
  .identity {
    margin-top: 26px;
    display: flex;
    flex-direction: column;
    align-items: flex-end;
  }
  .identity__name {
    font-family: "Parisienne", cursive;
    font-size: 40px;
    color: var(--gold);
    line-height: 1;
  }
  .identity__title {
    font-family: "Montserrat", sans-serif;
    font-weight: 400;
    font-size: 13px;
    color: var(--ink);
    margin-top: 2px;
    margin-right: 4px;
  }
  .card--back .identity { margin-top: 16px; }
  .card--back .identity__title { color: var(--gold-light); }
  .contact {
    margin-top: 34px;
    display: flex;
    gap: 28px;
    font-family: "Montserrat", sans-serif;
    font-size: 12px;
    color: var(--ink);
  }
  .contact__item {
    display: flex;
    align-items: center;
    gap: 7px;
  }
  .contact__icon { width: 13px; height: 11px; }
</style>
</head>
<body>
<main class="canvas">
  <section class="card card--front">
    <div class="monogram">LV</div>
    <div class="identity">
      <div class="identity__name">Lydia Vandermere</div>
      <div class="identity__title">Justice of the Peace</div>
    </div>
    <div class="contact">
      <span class="contact__item">
        <svg class="contact__icon" viewBox="0 0 13 11" aria-hidden="true">
          <path d="M1 4 Q6.5 -0.5 12 4 L10.5 5.5 L9 4.2 L4 4.2 L2.5 5.5 Z" fill="#b8921f"/>
          <rect x="2.5" y="5.5" width="8" height="5" rx="1" fill="#b8921f"/>
          <circle cx="6.5" cy="8" r="1.3" fill="#f4f0e3"/>
        </svg>
        0412555038
      </span>
      <span class="contact__item">
        <svg class="contact__icon" viewBox="0 0 13 11" aria-hidden="true">
          <rect x="0.5" y="1.5" width="12" height="8" fill="#b8921f"/>
          <path d="M0.5 1.5 L6.5 6 L12.5 1.5" fill="none" stroke="#f4f0e3" stroke-width="1"/>
        </svg>
        lydia@vandermerehouse.com
      </span>
    </div>
  </section>

  <section class="card card--back">
    <div class="monogram">LV</div>
    <div class="identity">
      <div class="identity__name">Lydia Vandermere</div>
      <div class="identity__title">Justice of the Peace</div>
    </div>
  </section>
</main>
</body>
</html>
```